Hardcore nerd needs to stand out in a sea of dull Defence business cards

Wombat Devices is a new Australian consulting engineering company that turns research and theory into practical systems. No evangelistic fluff, just mathematics and physics into electronic and optical circuits for consumer products, scientific research or Defence applications.

We already have a recognised logo (provided) which is often dark blue/black on a light background but we're open to other combinations. (Us engineers tend to have limited aesthetic imagination :)

Some of our recent products have included:
* Instrumentation for electrical testing,
* Radar jammers,
* GPS antenna design,
* Satellite tracking systems,
* High power lasers

We're open to both single and double-sided designs - happy to be convinced either way.

P.S. Another group is working on the web page, so - alas - our web site is currently of no use for images/ideas...

Target Market(s)

Engineering managers,
Scientists

Contact Information for Business Card

Dr Colin Marsh
R&D Engineer

colin@wombatdevicesco.com.au
0427 563 210

PO Box XXX (to be confirmed)
Banks ACT 2913
Australia

Font styles to use
Serif
Sans Serif

Colors

Designer to choose colors to be used in the design.

Requirements
Must have
• My contact details!
• I've had many (great) "bold and plain" designs submitted already, so feel free to be artistically creative :)
• Happy to take advice re fonts/colours/printability etc.
Nice to have
• I'm not sure if "lists" are more at home on a CV than a business card, but representative services include:
• Applied electromagnetics
• RF and high speed electronics
• Signal and image processing
• Electro-optical and laser systems
• Concept-to-prototype design services
• If you're considering double sided cards, then often measuring/alignment grids/rulers feature on the back of similar cards.
• e.g. https://www.lumoptix-example.com/newgrouppage9.cfm?objectgroup_id=4815
• https://www.lumoptix-example.com/newgrouppage9.cfm?objectgroup_ID=4817
• ..or even a "Smith chart" (google will return lots)
• Generic images to represent a capability might work - googling images associated with keyword for each of these areas might help:
• - "passive radar", "phased array", "fdtd", "vircator"
• RF and high speed electronic design
• - "smith chart", "microstrip circuits", "dimensioned drawing", "electronic schematic"
• - "dft", "iir filter"
• - "optical cavity". "laser energy level diagram"
• Background/watermarked images outlines/wireframes/schematics would probably look OK.
Should not have
• If a list of projects/services is provided, it is important not to make the client feel that this is "all" the company can do. Engineering design is a creative discipline (like graphics :)
• Please, no stock "military" snaps like planes, missiles, etc!

```html
<!DOCTYPE html>
<html lang="en">
<head>
<meta charset="utf-8">
<title>Wombat Devices – Business Card</title>
<link href="https://fonts.googleapis.com/css2?family=Roboto+Condensed:wght@400;700&display=swap" rel="stylesheet">
<style>
  :root {
    --navy: #232a6e;
    --navy-deep: #1e2563;
    --paper: #ffffff;
    --ink-grey: #6a6a70;
    --stage: #e9eaee;
    --on-navy: #ffffff;
  }
  * { box-sizing: border-box; margin: 0; padding: 0; }
  html, body {
    width: 1200px; height: 900px; overflow: hidden;
    background: var(--stage);
    font-family: "Roboto Condensed", Arial, sans-serif;
  }
  .sheet {
    position: relative; width: 1200px; height: 900px;
    display: flex; align-items: center; justify-content: center; gap: 50px;
  }
  .card {
    position: relative; width: 540px; height: 310px; overflow: hidden;
    box-shadow: 0 6px 18px rgba(20, 24, 60, 0.18);
  }

  /* Front */
  .card--front { background: var(--paper); }
  .holder { position: absolute; left: 34px; top: 30px; }
  .holder__name { color: var(--navy); font-weight: 700; font-size: 19px; letter-spacing: 0.2px; }
  .holder__role { color: var(--ink-grey); font-size: 14px; margin-top: 2px; }
  .holder__rule { width: 12px; height: 2px; background: var(--navy); margin: 12px 0 12px; }
  .contact { list-style: none; }
  .contact li { display: flex; align-items: center; gap: 8px; color: var(--ink-grey); font-size: 14px; line-height: 19px; }
  .contact svg { width: 12px; height: 12px; flex: none; }
  .address { position: absolute; left: 34px; top: 206px; color: var(--ink-grey); font-size: 14px; line-height: 18px; }
  .front-band {
    position: absolute; left: 0; bottom: 0; width: 250px; height: 24px; background: var(--navy);
  }
  .brand {
    position: absolute; display: flex; align-items: center; gap: 10px;
    color: var(--navy); font-weight: 700; text-transform: uppercase; letter-spacing: 1px;
  }
  .brand__dot { border-radius: 50%; background: currentColor; flex: none; }
  .card--front .brand { right: 34px; bottom: 38px; font-size: 28px; }
  .card--front .brand__dot { width: 40px; height: 40px; }

  /* Back */
  .card--back { background: var(--navy); }
  .back-texture {
    position: absolute; inset: 0;
    background: linear-gradient(135deg, var(--navy) 0%, var(--navy-deep) 100%);
  }
  .card--back .brand { color: var(--on-navy); right: 60px; top: 108px; font-size: 24px; }
  .card--back .brand__dot { width: 30px; height: 30px; }
  .services {
    position: absolute; left: 28px; right: 20px; bottom: 26px;
    color: var(--on-navy); font-size: 13.5px; line-height: 19px;
  }
  .services p::before { content: ""; }
  .services span::before {
    content: ""; display: inline-block; width: 5px; height: 5px; background: var(--on-navy);
    margin: 0 5px 2px 0; vertical-align: middle;
  }
  .services span { margin-right: 8px; }
  .services .second { padding-left: 20px; }
</style>
</head>
<body>
<main class="sheet">
  <section class="card card--front" aria-label="Business card front">
    <div class="holder">
      <h1 class="holder__name">DR COLIN MARSH</h1>
      <p class="holder__role">R&amp;D Engineer</p>
      <div class="holder__rule"></div>
      <ul class="contact">
        <li>
          <svg viewBox="0 0 12 12" aria-hidden="true"><circle cx="6" cy="6" r="5.2" fill="none" stroke="#232a6e" stroke-width="1.2"/><path d="M4.2 3.4l1 1-.6.8a3.5 3.5 0 0 0 1.9 1.9l.8-.6 1 1-.7.8C5.6 8.2 3.8 6.4 3.5 4.1z" fill="#232a6e"/></svg>
          0427 563 210
        </li>
        <li>
          <svg viewBox="0 0 12 12" aria-hidden="true"><rect x="1" y="2.5" width="10" height="7" fill="none" stroke="#232a6e" stroke-width="1.1"/><path d="M1 2.5l5 4 5-4" fill="none" stroke="#232a6e" stroke-width="1.1"/></svg>
          colin@wombatdevicesco.com.au
        </li>
        <li>
          <svg viewBox="0 0 12 12" aria-hidden="true"><circle cx="6" cy="6" r="5.2" fill="#232a6e"/><path d="M0.8 6h10.4M6 0.8v10.4M6 .8c-2.4 2.8-2.4 7.6 0 10.4M6 .8c2.4 2.8 2.4 7.6 0 10.4" fill="none" stroke="#fff" stroke-width="0.7"/></svg>
          www.wombatdevicesco.com.au
        </li>
      </ul>
    </div>
    <address class="address">PO Box XXX<br>Banks ACT 2913, Australia</address>
    <div class="front-band"></div>
    <div class="brand"><span class="brand__dot"></span>Wombat Devices</div>
  </section>

  <section class="card card--back" aria-label="Business card back">
    <div class="back-texture" role="img" aria-label="Faint repeating brand pattern over dark blue"></div>
    <div class="brand"><span class="brand__dot"></span>Wombat Devices</div>
    <div class="services">
      <p><span>Applied electromagnetics</span><span>RF and high speed electronics</span><span>Signal and image processing</span></p>
      <p class="second"><span>Electro-optical and laser systems</span><span>Concept-to-prototype design services</span></p>
    </div>
  </section>
</main>
</body>
</html>
```